Architectural, Engineering and Design Build

Tovantek4.com
Veteran Disabled Certified company is doing business in Architecture, Engineer and Design build - look simialr websites and come up with design follow following website
https://harlow-vessant.example/
https://www.quenforgroup.example/
https://www.ddelbmx.example/contract-vehicles/service-disabled-veteran-owned-small-business-sdvosb/
https://www.ostrelgrouplink.example/about/sdvosb/

Target Market(s)

US - Defense and Federal Government

Industry/Entity Type

Colors
0054AA
0677BA
7BADD7
CADEEF
E8F1F8

Requirements
Must have
• Army, American patriotism , Buildings, construction, architecture, engineering
Nice to have
• I need to attract federal government agencies and Defense

```html
<!DOCTYPE html>
<html lang="en">
<head>
<meta charset="utf-8">
<title>Tovantek4.com — Architecture, Engineering and Design Build</title>
<link rel="stylesheet" href="https://fonts.googleapis.com/css2?family=Lexend:wght@400;500;600&family=Inter:wght@400;500;600;700&display=swap">
<style>
:root{
  --blue:#0054AA;
  --blue-2:#0677BA;
  --blue-3:#7BADD7;
  --blue-4:#CADEEF;
  --blue-5:#E8F1F8;
  --panel:#F1F6FB;
  --ink:#1B1F2A;
  --text:#5C6270;
  --line:#D9DFE7;
  --white:#FFFFFF;
  --star:#F5A524;
  --red:#D6322B;
}
*{margin:0;padding:0;box-sizing:border-box}
html,body{width:1200px;height:4608px;overflow:hidden;background:var(--white)}
body{position:relative;font-family:"Inter",sans-serif;color:var(--text)}
.abs{position:absolute}
h1,h2,h3{font-family:"Lexend",sans-serif;font-weight:500;color:var(--ink)}
.eyebrow{position:absolute;display:flex;align-items:center;gap:8px;font-size:11px;font-weight:600;letter-spacing:1.4px;text-transform:uppercase;color:var(--blue)}
.eyebrow::before{content:"";width:32px;height:2px;background:var(--blue)}
.btn-outline{position:absolute;display:flex;align-items:center;justify-content:center;gap:8px;border:1.5px solid var(--blue);color:var(--blue);font-size:12px;font-weight:600;letter-spacing:1.4px;text-transform:uppercase;background:var(--white)}
.arrow{font-family:"Inter",sans-serif}

/* hero */
.hero-photo{left:84px;top:0;width:1116px;height:658px;background:linear-gradient(180deg,#2b3642 0%,#46525c 45%,#3a3f44 75%,#24282c 100%)}
.hero-photo::after{content:"";position:absolute;inset:0;background:linear-gradient(90deg,rgba(10,16,26,.55),rgba(10,16,26,.15))}
.brand{position:absolute;display:flex;align-items:center;gap:12px;font-family:"Lexend",sans-serif;font-weight:500}
.brand .mark{background:var(--blue);border-radius:50%}
.nav{left:564px;top:40px;display:flex;gap:40px;font-size:13px;font-weight:600;letter-spacing:1.2px;color:var(--white)}
.nav .active{position:relative}
.nav .active::before{content:"";position:absolute;left:0;right:0;top:-9px;height:2px;background:var(--red)}
.nav-cta{left:967px;top:29px;width:147px;height:46px;border:1.5px solid var(--white);color:var(--white);display:flex;align-items:center;justify-content:center;font-size:13px;font-weight:600;letter-spacing:1.2px}
.hero-title{left:105px;top:232px;width:560px;font-size:42px;line-height:51px;color:var(--white)}
.hero-btn{left:105px;top:424px;width:172px;height:50px;background:var(--blue);color:var(--white);display:flex;align-items:center;justify-content:center;font-size:12px;font-weight:600;letter-spacing:1.4px}
.thumb-strip{left:844px;top:582px;width:356px;height:76px;background:var(--white)}
.thumb{top:590px;height:68px}

/* about */
.about-title{left:86px;top:748px;width:460px;font-size:35px;line-height:45px}
.about-text{left:587px;top:754px;width:520px;font-size:14px;line-height:25px}

.plan-photo{left:0;top:948px;width:1114px;height:364px;background:linear-gradient(120deg,#4b4a45 0%,#9c978c 40%,#c9c3b6 60%,#6b6a66 100%)}

/* projects */
.projects-band{left:84px;top:1314px;width:1116px;height:438px;background:var(--panel)}
.section-title{font-size:34px;line-height:43px}
.project-card{position:absolute;top:1471px;width:322px;height:448px;background:var(--white);box-shadow:0 6px 20px rgba(20,40,70,.08)}
.project-card .photo{height:240px}
.project-card h3{position:absolute;left:18px;top:256px;width:290px;font-family:"Inter",sans-serif;font-size:14px;line-height:23px;font-weight:600}
.project-card p{position:absolute;left:18px;top:312px;width:290px;font-size:14px;line-height:25px}
.project-card .btn-outline{left:18px;top:376px;width:168px;height:50px}

/* why */
.why-photo{left:572px;top:2026px;width:485px;height:554px;background:linear-gradient(135deg,#e6e6e6 0%,#bdbdbd 55%,#8e8e8e 100%)}
.why-box{left:141px;top:2080px;width:487px;height:441px;background:var(--panel)}
.why-title{left:188px;top:2150px;width:400px;font-size:34px;line-height:44px}
.why-text{left:188px;top:2246px;width:405px;font-size:14px;line-height:25px}
.badge{left:180px;top:2386px;width:112px;height:104px;border-radius:50%;border:3px solid var(--blue);background:var(--white)}

/* services */
.services-photo{left:0;top:2630px;width:1200px;height:388px;background:linear-gradient(90deg,#2c3a4b 0%,#3c4856 50%,#2a3340 100%)}
.services-photo::after{content:"";position:absolute;inset:0;background:rgba(20,34,52,.55)}
.services-base{left:0;top:3018px;width:1200px;height:483px;background:var(--panel)}
.service-card{position:absolute;top:2830px;width:324px;height:380px;background:var(--white);text-align:center;box-shadow:0 6px 20px rgba(20,40,70,.06)}
.service-card svg{position:absolute;left:117px;top:50px}
.service-card h3{position:absolute;left:0;right:0;top:150px;font-size:17px;font-family:"Inter",sans-serif;font-weight:500}
.service-card p{position:absolute;left:30px;right:30px;top:188px;font-size:14px;line-height:25px}
.service-card .btn-outline{left:78px;top:283px;width:168px;height:50px}
.partners{left:84px;top:3285px;width:1030px;height:132px;border:1px solid var(--blue-3);display:grid;grid-template-columns:repeat(4,1fr);background:var(--white)}
.partner{border-right:1px solid var(--blue-3);display:flex;align-items:center;justify-content:center}
.partner:last-child{border-right:none}
.partner span{width:150px;height:50px;background:var(--blue-4);border-radius:4px}

/* testimonials */
.map-pattern{left:40px;top:3570px;width:1120px;height:560px;background:radial-gradient(ellipse at center,rgba(202,222,239,.55) 0%,rgba(232,241,248,.3) 55%,rgba(255,255,255,0) 75%)}
.testi-card{position:absolute;top:3719px;width:331px;height:322px;background:var(--white);text-align:center;box-shadow:0 6px 24px rgba(20,40,70,.08)}
.avatar{position:absolute;left:139px;top:28px;width:52px;height:52px;border-radius:50%;background:var(--blue);color:var(--white);font-weight:600;font-size:17px;display:flex;align-items:center;justify-content:center}
.testi-card h3{position:absolute;left:0;right:0;top:80px;font-family:"Inter",sans-serif;font-size:17px;font-weight:600}
.testi-card .role{position:absolute;left:0;right:0;top:106px;font-size:12px}
.stars{position:absolute;left:0;right:0;top:124px;color:var(--star);font-size:15px;letter-spacing:1px}
.testi-card blockquote{position:absolute;left:32px;right:32px;top:157px;font-size:14px;line-height:23px}
.source{position:absolute;left:155px;top:267px;width:20px;height:20px;border-radius:50%;background:var(--blue-3)}

/* footer */
.footer{left:0;top:4159px;width:1200px;height:449px;background:var(--panel)}
.to-top{left:1020px;top:4201px;font-size:11px;font-weight:700;letter-spacing:1.4px;color:var(--ink)}
.footer-rule{left:84px;top:4234px;width:1030px;height:1px;background:var(--line)}
.footer h4{position:absolute;top:4306px;font-size:14px;font-weight:600;color:var(--blue);letter-spacing:.5px}
.footer ul{position:absolute;list-style:none;font-size:13.5px;line-height:30px;color:var(--text)}
.social{position:absolute;top:4406px;width:36px;height:36px;border:1.5px solid var(--blue-3)}
.legal{top:4564px;font-size:12px;color:var(--text)}
.legal b{color:var(--blue);font-weight:500}
</style>
</head>
<body>

<!-- HERO -->
<div class="abs hero-photo" role="img" aria-label="Photo of a glass and stone federal government building at dusk"></div>
<div class="brand" style="left:104px;top:16px;font-size:30px;color:var(--white)">
  <span class="mark" style="width:62px;height:62px"></span>Tovantek4.com
</div>
<nav class="abs nav">
  <span class="active">HOME</span><span>ABOUT</span><span>SERVICES</span><span>PROJECTS</span>
</nav>
<div class="abs nav-cta">CONTACT</div>
<h1 class="abs hero-title">Architecture For federal Government Agencies and Defense</h1>
<div class="abs hero-btn">OUR PROJECTS <span class="arrow">&nbsp;→</span></div>
<div class="abs thumb-strip"></div>
<div class="abs thumb" style="left:846px;width:86px;background:linear-gradient(180deg,#6fa6d6,#c7a26b)" role="img" aria-label="Thumbnail of a modern office building"></div>
<div class="abs thumb" style="left:940px;width:85px;background:linear-gradient(180deg,#8fb9e3,#e9e7e2)" role="img" aria-label="Thumbnail of a white columned government building"></div>
<div class="abs thumb" style="left:1032px;width:82px;background:linear-gradient(135deg,#f2f0ea,#c9b27a)" role="img" aria-label="Thumbnail of drafting tools on plans"></div>

<!-- ABOUT -->
<div class="eyebrow" style="left:86px;top:730px">About Us</div>
<h2 class="abs about-title">We Design and Build Federal Government Agencies and Defense</h2>
<p class="abs about-text">Lorem ipsum dolor sit amet, consectetur adipiscing elit. Quisque congue eros rhoncus nulla consequat, in rhoncus massa finibus. Cras tempus arcu leo, eu condimentum diam sollicitudin vel.</p>
<div class="btn-outline" style="left:587px;top:855px;width:184px;height:50px">READ MORE <span class="arrow">→</span></div>

<div class="abs plan-photo" role="img" aria-label="Photo of hands drawing an architectural floor plan with a pencil beside a calculator"></div>

<!-- PROJECTS -->
<div class="abs projects-band"></div>
<div class="eyebrow" style="left:105px;top:1352px">Project</div>
<h2 class="abs section-title" style="left:105px;top:1370px;width:420px">Best Project That We’ve Completed</h2>
<svg class="abs" style="left:1074px;top:1400px" width="38" height="24" viewBox="0 0 38 24"><path d="M2 12h32M24 3l10 9-10 9" fill="none" stroke="#0054AA" stroke-width="2.4"/></svg>

<article class="project-card" style="left:105px">
  <div class="photo" style="background:linear-gradient(180deg,#5b94d4 0%,#cfd6dc 55%,#6f7a5a 100%)" role="img" aria-label="Photo of a white neoclassical domed museum building"></div>
  <h3>Federal Works Directorate, Ridgefield District, SDVOSB Multiple Award Task</h3>
  <p>Aliquam consequat mi non ex viverra placerat. Duis uleu leo nec accumsan.</p>
  <div class="btn-outline">READ MORE <span class="arrow">→</span></div>
</article>
<article class="project-card" style="left:449px">
  <div class="photo" style="background:linear-gradient(180deg,#1f5fbf 0%,#6d9ee0 45%,#dcdcdc 75%,#8a8a8a 100%)" role="img" aria-label="Photo of a long white colonnaded federal office building"></div>
  <h3>Federal Works Directorate, Ridgefield District, SDVOSB Multiple Award Task</h3>
  <p>Aliquam consequat mi non ex viverra placerat. Duis uleu leo nec accumsan.</p>
  <div class="btn-outline">READ MORE <span class="arrow">→</span></div>
</article>
<article class="project-card" style="left:792px">
  <div class="photo" style="background:linear-gradient(180deg,#9cb4cc 0%,#e6d9bf 45%,#a58c6e 80%,#6d5a48 100%)" role="img" aria-label="Photo of a classical stone building with a row of columns"></div>
  <h3>Federal Works Directorate, Ridgefield District, SDVOSB Multiple Award Task</h3>
  <p>Aliquam consequat mi non ex viverra placerat. Duis uleu leo nec accumsan.</p>
  <div class="btn-outline">READ MORE <span class="arrow">→</span></div>
</article>

<!-- WHY CHOOSE US -->
<div class="abs why-photo" role="img" aria-label="Photo of architectural drawings with a compass, protractor, pen and eyeglasses"></div>
<div class="abs why-box"></div>
<div class="eyebrow" style="left:188px;top:2130px">Why Choose Us</div>
<h2 class="abs why-title">Let's start your next project today</h2>
<p class="abs why-text">Integer sit amet ex ac nuncrices maximus in ut orci. Sed commodo condimtum nisl, in dignissim ante bibendum ac. Fusce eget turpis sit amilisis rhoncus. Pellentesque nec dui ultrices. Sed posuere quam in augue faucibus, nec elementum dolor posuere.</p>
<div class="abs badge" role="img" aria-label="Certification badge"></div>

<!-- SERVICES -->
<div class="abs services-photo" role="img" aria-label="Photo of an American flag in front of a government building"></div>
<div class="abs services-base"></div>
<div class="eyebrow" style="left:84px;top:2727px;color:var(--white)">Our Services</div>
<h2 class="abs section-title" style="left:84px;top:2746px;color:var(--white)">We Provide Quality Services</h2>

<article class="service-card" style="left:84px">
  <svg width="90" height="80" viewBox="0 0 90 80"><circle cx="60" cy="24" r="22" fill="#E8F1F8"/><g fill="none" stroke="#0054AA" stroke-width="2"><rect x="14" y="22" width="50" height="40"/><path d="M14 30h50M24 22v40M34 40h22v14H34z"/><path d="M10 66h60"/></g></svg>
  <h3>Architecture Design</h3>
  <p>Fusce eget tus sit amilisis rhoncus. Pellentesque nec dui ultrices. Sed posuere quam</p>
  <div class="btn-outline">READ MORE <span class="arrow">→</span></div>
</article>
<article class="service-card" style="left:438px">
  <svg width="90" height="80" viewBox="0 0 90 80"><circle cx="60" cy="24" r="22" fill="#E8F1F8"/><g fill="none" stroke="#0054AA" stroke-width="2"><circle cx="40" cy="40" r="22"/><circle cx="40" cy="40" r="12"/><path d="M40 12v6M40 62v6M12 40h6M62 40h6M20 20l4 4M56 56l4 4M20 60l4-4M56 24l4-4"/><path d="M34 44v-6l6-4 6 4v6z"/></g></svg>
  <h3>Engineer</h3>
  <p>Fusce eget tus sit amilisis rhoncus. Pellentesque nec dui ultrices. Sed posuere quam</p>
  <div class="btn-outline">READ MORE <span class="arrow">→</span></div>
</article>
<article class="service-card" style="left:792px">
  <svg width="90" height="80" viewBox="0 0 90 80"><circle cx="60" cy="24" r="22" fill="#E8F1F8"/><g fill="none" stroke="#0054AA" stroke-width="2"><path d="M28 30a12 12 0 0 1 24 0"/><path d="M40 12v6M22 30h36v6H22zM16 62h48M18 66h44"/><path d="M24 36v24M32 36v24M40 36v24M48 36v24M56 36v24"/></g></svg>
  <h3>Design Build</h3>
  <p>Fusce eget tus sit amilisis rhoncus. Pellentesque nec dui ultrices. Sed posuere quam</p>
  <div class="btn-outline">READ MORE <span class="arrow">→</span></div>
</article>

<div class="abs partners">
  <div class="partner" role="img" aria-label="Partner badge"><span></span></div>
  <div class="partner" role="img" aria-label="Partner badge"><span></span></div>
  <div class="partner" role="img" aria-label="Partner badge"><span></span></div>
  <div class="partner" role="img" aria-label="Partner badge"><span></span></div>
</div>

<!-- TESTIMONIALS -->
<div class="abs map-pattern" role="img" aria-label="Faint dotted world map decoration"></div>
<div class="eyebrow" style="left:84px;top:3632px">Testimonials</div>
<h2 class="abs section-title" style="left:84px;top:3650px">What People Say About Us</h2>

<article class="testi-card" style="left:84px">
  <div class="avatar">L</div><h3>Lenn Aubrecht</h3><div class="role">CEO</div><div class="stars">★★★★★</div>
  <blockquote>"Aliquam condimentum urna vel velit sodales, in sollicitudin ex lacinia. Suspendisse sit amet mi ultricies, ultrices libero nec, vehicula augue."</blockquote>
  <span class="source"></span>
</article>
<article class="testi-card" style="left:434px">
  <div class="avatar">L</div><h3>Lenn Aubrecht</h3><div class="role">CEO</div><div class="stars">★★★★★</div>
  <blockquote>"Aliquam condimentum urna vel velit sodales, in sollicitudin ex lacinia. Suspendisse sit amet mi ultricies, ultrices libero nec, vehicula augue."</blockquote>
  <span class="source"></span>
</article>
<article class="testi-card" style="left:785px">
  <div class="avatar">L</div><h3>Lenn Aubrecht</h3><div class="role">CEO</div><div class="stars">★★★★★</div>
  <blockquote>"Aliquam condimentum urna vel velit sodales, in sollicitudin ex lacinia. Suspendisse sit amet mi ultricies, ultrices libero nec, vehicula augue."</blockquote>
  <span class="source"></span>
</article>

<!-- FOOTER -->
<footer class="abs footer"></footer>
<div class="abs to-top">↑ GO TO TOP</div>
<div class="abs footer-rule"></div>
<div class="brand" style="left:84px;top:4320px;font-size:30px;color:var(--ink)">
  <span class="mark" style="width:64px;height:64px"></span>Tovantek4.com
</div>
<span class="social" style="left:137px" aria-label="Social profile"></span>
<span class="social" style="left:187px" aria-label="Social profile"></span>
<span class="social" style="left:234px" aria-label="Social profile"></span>

<div class="footer">
  <h4 style="left:431px">CONTACT INFO</h4>
  <ul style="left:431px;top:4346px">
    <li>12 Harbor Row, Norfield</li><li>Norfield, Australia</li><li style="margin-top:2px">info@tovantek4.com</li><li>1800 555 019</li>
  </ul>
  <h4 style="left:746px">QUICK LINKS</h4>
  <ul style="left:746px;top:4346px">
    <li>Home</li><li>About</li><li>Services</li><li>Projects</li><li>Contact</li>
  </ul>
  <h4 style="left:979px">SERVICES</h4>
  <ul style="left:979px;top:4346px">
    <li>Architecture Design</li><li>Engineer</li><li>Design Build</li>
  </ul>
</div>
<div class="abs legal" style="left:84px">© 2024 <b>Tovantek4.com</b>. All right reserved</div>
<div class="abs legal" style="left:967px">June 18, 2024. Layout_4</div>

</body>
</html>
```